Large Financial Advisory Firm Needs a Brochure!

We are looking for a modern and professional 4 page brochure for our Financial Advisory firm, Harbrook Counsel Group. I've attached multiple files to help with the completion of the design.
SIZE OF BROCHURE: 17 x 11 FLAT, 8.5 x 11 inch FOLDED
1. A PDF titled Design Brief will provide you with an overview of the project, the text to be included in the brochure and other misc. instructions.
2. Logo Files, you will need to incorporate our logo into the brochure design, I've attached all the files please select the images that suit your design.
3. Competitor Illustration - I've attached an image that needs to be included on the 2nd page (inside left cover of the brochure). You will need to incorporate the pros/cons of using our competitors and the advantages of using our firm. This is outlined in the Design Brief PDF.
NOTE: If possible please get rid of the blue sky in the illustration. Just use the buildings, the blue throws off the concept. I contacted the illustrator and am waiting for a design without the sky but it may not be ready in time so please delete it if possible.
- I like the Avenir fonts, 85 Heavy, 65 Medium and 45.

```html
<!DOCTYPE html>
<html lang="en">
<head>
<meta charset="utf-8">
<title>Harbrook Counsel Group – Succession Partnership</title>
<link href="https://fonts.googleapis.com/css2?family=Nunito+Sans:wght@700;800&family=Questrial&display=swap" rel="stylesheet">
<style>
  :root {
    --stage: #e9e9ea;
    --paper: #fbfbfb;
    --ink: #262626;
    --heading: #1c1c1c;
    --link: #1d2a6b;
    --rule: #c9c9cc;
    --gold-light: #f3c600;
    --gold-deep: #f2b232;
    --brand-text: #ffffff;
  }
  * { margin: 0; padding: 0; box-sizing: border-box; }
  html, body {
    width: 1000px; height: 1200px; overflow: hidden;
    background: var(--stage);
  }
  .page {
    position: absolute; left: 50px; top: 18px;
    width: 900px; height: 1164px;
    background: var(--paper);
    overflow: hidden;
    font-family: "Questrial", "Century Gothic", sans-serif;
    color: var(--ink);
    font-size: 15.4px;
    line-height: 17.35px;
  }
  .page-swoosh { position: absolute; left: 0; top: 0; width: 900px; height: 1164px; }
  .content { position: absolute; left: 81px; top: 34px; width: 790px; }
  .title {
    font-family: "Nunito Sans", "Avenir", sans-serif;
    font-weight: 800; font-size: 21.5px; line-height: 26px;
    color: var(--heading); margin-bottom: 13px;
  }
  .body-block { margin-left: 31px; }
  .body-block p { margin-bottom: 17.35px; }
  .body-block strong, .subhead {
    font-family: "Nunito Sans", "Avenir", sans-serif; font-weight: 700;
  }
  .subhead { font-size: 15.4px; margin-bottom: 17.35px; color: var(--heading); }
  .bullets { list-style: none; margin-left: 10px; margin-bottom: 17.35px; }
  .bullets li { position: relative; padding-left: 13px; }
  .bullets li::before { content: "•"; position: absolute; left: 0; }
  .contact { margin-left: 168px; margin-top: -17.35px; }
  .contact a { color: var(--link); text-decoration: none; }
  .brand-name {
    position: absolute; left: 37px; top: 1086px;
    font-family: "Questrial", "Century Gothic", sans-serif;
    color: var(--brand-text);
  }
  .brand-name .brand-main {
    display: block; font-size: 37px; line-height: 38px; letter-spacing: 2px;
  }
  .brand-name .brand-sub {
    display: block; font-size: 13.5px; line-height: 16px; letter-spacing: 5.2px;
    margin-top: 2px;
  }
</style>
</head>
<body>
<div class="page">
  <svg class="page-swoosh" viewBox="0 0 1038 1340" preserveAspectRatio="none" aria-hidden="true">
    <defs>
      <linearGradient id="gold" x1="0" x2="1" y1="0" y2="0">
        <stop offset="0" stop-color="var(--gold-light)"/>
        <stop offset="1" stop-color="var(--gold-deep)"/>
      </linearGradient>
    </defs>
    <path d="M0 1078 Q 520 1300 1038 1186" fill="none" stroke="var(--rule)" stroke-width="2"/>
    <path d="M0 1124 Q 560 1330 1038 1236 L1038 1340 L0 1340 Z" fill="url(#gold)"/>
  </svg>

  <div class="content">
    <h1 class="title">The Harbrook Difference:</h1>
    <div class="body-block">
      <p>We put <strong>YOU</strong> at the center of the process.</p>
      <p><strong>You</strong> are the expert, we do not want to impose a client experience, investment<br>philosophy, or planning process on your firm. We provide the raw talent, and we need<br>your help to build them into the successor your clients deserve.</p>
      <p><strong>You</strong> have a voice, we want you to participate in the strategic direction of the firm and<br>offer a number of ways for you to continue doing what you love.</p>
      <p><strong>You</strong>, your clients, your staff, and the incoming advisor are the most important aspect<br>of the succession process.</p>
      <p><strong>You</strong> set the pace, we will work on your timeline. We create personalized solutions<br>based on your succession readiness.</p>

      <h2 class="subhead">What We Offer</h2>
      <ul class="bullets">
        <li>A successor that your clients deserve and you select. Incoming advisors will<br>have 10+ years of industry experience, a CFA, CFP, CPA and/or MBA with<br>extensive training in capital markets, financial planning, and behavioral<br>communication</li>
        <li>A culture that balances freedom of choice with the responsibility to perform</li>
        <li>The capital backing of a large organization without the associated bureaucracy</li>
        <li>Flexibility, it is ingrained in our culture and a critical element of the succession<br>planning process</li>
        <li>Creative ways to structure the succession plan, we allow you to participate in the<br>upside of the business</li>
        <li>A unique offering for internal succession which equitizes staff and provides you<br>with a fair value for your business</li>
        <li>A well-qualified team with M&amp;A experience across multiple industries</li>
        <li>Centralized investment, operations, and compliance to free up your time to<br>focus on what you love to do</li>
        <li>A true partnership, we offer strategic consulting agreements for advisors who<br>want to continue working in retirement</li>
        <li>A dedicated transition team to help with the integration between firms</li>
      </ul>

      <h2 class="subhead">Ideal Partner</h2>
      <p>Finding a firm that shares your values is difficult. We employ a mutual due diligence<br>process to ensure there is a cultural, philosophical and personal fit, we look for<br>advisors who:</p>
      <ul class="bullets">
        <li>Care deeply about their clients and place client interests above all else</li>
        <li>Engage clients in a comprehensive wealth management process which may<br>include: estate, tax, insurance, social security, and investment planning.</li>
        <li>Utilize investment solutions that provide low cost, tax-efficient, diversified<br>exposure to capital markets</li>
        <li>Understand that behavioral coaching is a critical part of the financial planning<br>process and work to educate clients on the benefits of discipline</li>
        <li>Value mentoring and could potentially take an active role training their successor</li>
      </ul>
      <p>If you share some or all of the above characteristics, reach out to us and start a<br>conversation today.</p>
      <p class="contact">(Include Contact Information)<br>Daniel Marsh, Founder, 555-014-2387, <a href="mailto:daniel.marsh@harbrookcg.com">daniel.marsh@harbrookcg.com</a></p>
    </div>
  </div>

  <div class="brand-name">
    <span class="brand-main">HARBROOK</span>
    <span class="brand-sub">COUNSEL GROUP</span>
  </div>
</div>
</body>
</html>
```